Heritage Hollow Business Cards

Require a business card design. <br/><br/>Needs to include logo (either round or long version) plus these details:<br/>Maya Torvel<br/>Heritage Hollow<br/>maya@quonbrook.com.au<br/>02 6481 7390<br/>PO Box Glenwarra NSW 2913<br/>www.heritagehollow.com.au<br/><br/>I need in an editable format so that I can create for multiple staff members. <br/><br/>

Target Market(s)

We are an online store selling renovation products to home owners are builders. Looking for a classic classy design.

Industry/Entity Type

Home And Garden

Contact Information for Business Card

Maya Torvel
Heritage Hollow
maya@quonbrook.com.au
02 6481 7390
PO Box Glenwarra NSW 2913
www.heritagehollow.com.au

Colors

Designer to choose colors to be used in the design.

Requirements
Must have
• Must include Logo.

```html
<!DOCTYPE html>
<html lang="en">
<head>
<meta charset="utf-8">
<title>Heritage Hollow Business Cards</title>
<link href="https://fonts.googleapis.com/css2?family=Gelasio:wght@400;600&display=swap" rel="stylesheet">
<style>
  :root {
    --backdrop: #d6d5db;
    --card: #151515;
    --copper: #94533c;
    --copper-deep: #7a3a2b;
    --copper-faint: #231917;
  }
  * { margin: 0; padding: 0; box-sizing: border-box; }
  html, body { width: 1200px; height: 1200px; overflow: hidden; }
  body {
    background: var(--backdrop);
    font-family: "Gelasio", Georgia, serif;
    color: var(--copper);
    position: relative;
  }
  .card {
    position: absolute;
    left: 225px;
    width: 750px;
    height: 450px;
    background: var(--card);
  }
  .card-front { top: 128px; }
  .card-back { top: 648px; }

  .contact {
    position: absolute;
    top: 24px;
    display: flex;
    align-items: center;
    gap: 8px;
    font-size: 17px;
    white-space: nowrap;
  }
  .contact svg { width: 18px; height: 18px; }
  .contact-phone { left: 30px; font-weight: 600; }
  .contact-email { right: 29px; }
  .contact-email svg { width: 24px; }

  .brand {
    position: absolute;
    left: 112px;
    top: 210px;
    display: flex;
    align-items: center;
    gap: 14px;
  }
  .brand-dot {
    width: 48px; height: 48px;
    border: 2px solid var(--copper);
    border-radius: 50%;
    flex: none;
  }
  .brand-name {
    font-size: 64px;
    font-weight: 400;
    line-height: 1;
    white-space: nowrap;
  }
  .website {
    position: absolute;
    left: 118px;
    top: 294px;
    display: flex;
    align-items: center;
    gap: 10px;
    font-size: 15px;
  }
  .website svg { width: 25px; height: 25px; }

  .address-row {
    position: absolute;
    left: 42px;
    right: 41px;
    top: 398px;
    display: flex;
    align-items: center;
    gap: 28px;
    font-size: 17px;
    white-space: nowrap;
  }
  .rule { flex: 1; height: 2px; background: var(--copper-deep); }

  .frame {
    position: absolute;
    left: 23px; top: 23px; right: 17px; bottom: 23px;
    border: 4px solid var(--copper);
  }
  .watermark {
    position: absolute;
    left: 217px; top: 66px;
    width: 316px; height: 316px;
    border: 2px solid var(--copper-faint);
    border-radius: 50%;
    display: flex;
    align-items: center;
    justify-content: center;
  }
  .watermark-name {
    color: var(--copper-faint);
    font-size: 44px;
    line-height: 1.05;
    text-align: center;
    margin-top: 140px;
  }
  .person {
    position: absolute;
    left: 223px;
    top: 188px;
    display: flex;
    align-items: center;
  }
  .person svg { width: 46px; height: 56px; }
  .person-divider {
    width: 2px; height: 72px;
    background: var(--copper);
    margin-left: 20px;
    margin-right: 18px;
  }
  .person-name {
    font-size: 50px;
    line-height: 1;
    white-space: nowrap;
  }
</style>
</head>
<body>

<section class="card card-front">
  <div class="contact contact-phone">
    <svg viewBox="0 0 24 24" fill="none" stroke="currentColor" stroke-width="1.6" stroke-linejoin="round">
      <path d="M5 3h4l2 5-2.5 1.5a11 11 0 0 0 6 6L16 13l5 2v4a2 2 0 0 1-2 2A16 16 0 0 1 3 5a2 2 0 0 1 2-2z"/>
    </svg>
    <span>02 6481 7390</span>
  </div>
  <div class="contact contact-email">
    <svg viewBox="0 0 28 20" fill="none" stroke="currentColor" stroke-width="1.8">
      <rect x="1" y="1" width="26" height="18"/>
      <path d="M1 1l13 10L27 1M1 19l10-9M27 19l-10-9"/>
    </svg>
    <span>maya@quonbrook.com.au</span>
  </div>

  <div class="brand">
    <span class="brand-dot"></span>
    <span class="brand-name">Heritage Hollow</span>
  </div>

  <div class="website">
    <svg viewBox="0 0 24 24" fill="none" stroke="currentColor" stroke-width="1.4">
      <circle cx="12" cy="12" r="10.5"/>
      <ellipse cx="12" cy="12" rx="4.5" ry="10.5"/>
      <path d="M1.5 12h21M3 7h18M3 17h18"/>
    </svg>
    <span>www.heritagehollow.com.au</span>
  </div>

  <div class="address-row">
    <span class="rule"></span>
    <span class="address">PO Box Glenwarra NSW 2913</span>
    <span class="rule"></span>
  </div>
</section>

<section class="card card-back">
  <div class="frame"></div>
  <div class="watermark">
    <span class="watermark-name">Heritage<br>Hollow</span>
  </div>
  <div class="person">
    <svg viewBox="0 0 46 56" fill="none" stroke="currentColor" stroke-width="3">
      <circle cx="23" cy="15" r="12"/>
      <path d="M10 30h26a8 8 0 0 1 8 8v10a6 6 0 0 1-6 6H8a6 6 0 0 1-6-6V38a8 8 0 0 1 8-8z"/>
    </svg>
    <span class="person-divider"></span>
    <span class="person-name">Maya Torvel</span>
  </div>
</section>

</body>
</html>
```